Brim Physiotherapy Business Card

I need a business card to allow for promotion of my new business as well as to book patients in for appointments.
The business is a pelvic floor health physiotherapy practice specialising in women's and men's continence type care.
It will be a small business offering personal care.
I will be the sole practitioner to start off with.

Target Market(s)

Pregnant and post natal women
Aging women and men
Women with breastfeeding difficulties
Children with bedwetting issues

Industry/Entity Type

Business

Contact Information for Business Card

Previous designs have perhaps been a bit too basic or not really eye catching.

Colors

Designer to choose colors to be used in the design.

Requirements
Must have
• Option to write appointment time and date on the back.
• Attractive and eye catching front.
• Logo somewhere on the card.
Nice to have
• Bright colours.
• Simple design that is easy to print.

```html
<!DOCTYPE html>
<html lang="en">
<head>
<meta charset="utf-8">
<title>Brim Physiotherapy – Business Card</title>
<link rel="stylesheet" href="https://fonts.googleapis.com/css2?family=Open+Sans:wght@400;600;700&display=swap">
<style>
  :root {
    --page-bg: #ecebe8;
    --card-white: #ffffff;
    --card-grey: #5f6063;
    --ink-grey: #6b6c6f;
    --ink-soft: #8a8b8e;
    --rule: #b9babc;
    --ink-white: #ffffff;
    --accent-lilac: #c9a6d9;
  }
  * { box-sizing: border-box; margin: 0; padding: 0; }
  html, body {
    width: 1200px; height: 1024px; overflow: hidden;
    background: var(--page-bg);
    font-family: "Open Sans", sans-serif;
  }
  .sheet {
    width: 1200px; height: 1024px;
    display: flex; flex-direction: column;
    align-items: center; justify-content: center; gap: 56px;
  }
  .card {
    width: 720px; height: 440px;
    position: relative;
    box-shadow: 0 6px 18px rgba(0,0,0,0.12);
  }

  /* Back: appointment side */
  .card--back { background: var(--card-white); color: var(--ink-grey); }
  .card--back .brand {
    position: absolute; left: 64px; top: 120px;
    display: flex; align-items: center; gap: 16px;
  }
  .brand__dot {
    width: 74px; height: 74px; border-radius: 50%;
    background: var(--ink-grey); flex: none;
  }
  .brand__name {
    font-weight: 700; font-size: 34px; line-height: 1.05;
    letter-spacing: -0.5px; color: var(--ink-grey);
  }
  .contact {
    position: absolute; left: 64px; top: 262px;
    list-style: none; font-size: 19px; color: var(--ink-grey);
  }
  .contact li { display: flex; align-items: center; gap: 12px; line-height: 38px; }
  .contact svg { width: 18px; height: 18px; fill: var(--ink-grey); flex: none; }
  .appointment {
    position: absolute; left: 430px; top: 130px; right: 56px;
    font-size: 18px; color: var(--ink-grey);
  }
  .appointment__field { display: flex; align-items: flex-end; gap: 10px; height: 76px; }
  .appointment__line { flex: 1; border-bottom: 1px solid var(--rule); height: 1px; margin-bottom: 6px; }

  /* Front: promotional side */
  .card--front { background: linear-gradient(135deg, #66676a 0%, var(--card-grey) 60%, #58595c 100%); color: var(--ink-white); }
  .card--front .brand {
    position: absolute; left: 96px; top: 96px;
    display: flex; align-items: center; gap: 22px;
  }
  .card--front .brand__dot { width: 112px; height: 112px; background: var(--ink-white); }
  .card--front .brand__name { color: var(--ink-white); font-size: 50px; }
  .tagline {
    position: absolute; left: 96px; top: 262px;
    font-size: 20px; line-height: 36px; color: var(--ink-white);
  }
</style>
</head>
<body>
<main class="sheet">

  <section class="card card--back" aria-label="Card back with appointment fields">
    <div class="brand">
      <span class="brand__dot"></span>
      <span class="brand__name">Brim<br>Physiotherapy</span>
    </div>
    <ul class="contact">
      <li>
        <svg viewBox="0 0 24 24" aria-hidden="true"><path d="M6.6 10.8a15 15 0 0 0 6.6 6.6l2.2-2.2c.3-.3.7-.4 1-.2 1.1.4 2.3.6 3.6.6.6 0 1 .4 1 1V20c0 .6-.4 1-1 1A17 17 0 0 1 3 4c0-.6.4-1 1-1h3.5c.6 0 1 .4 1 1 0 1.3.2 2.5.6 3.6.1.3 0 .7-.2 1z"/></svg>
        0412555018
      </li>
      <li>
        <svg viewBox="0 0 24 24" aria-hidden="true"><path d="M12 2a10 10 0 1 0 0 20 10 10 0 0 0 0-20zm6.9 6h-3a15 15 0 0 0-1.3-3.9A8 8 0 0 1 18.9 8zM12 4c.8 1.2 1.5 2.5 1.9 4h-3.8c.4-1.5 1.1-2.8 1.9-4zM4.3 14a8 8 0 0 1 0-4h3.4a16 16 0 0 0 0 4zm.8 2h3a15 15 0 0 0 1.3 3.9A8 8 0 0 1 5.1 16zm3-8h-3a8 8 0 0 1 4.3-3.9C8.8 5.3 8.4 6.6 8.1 8zM12 20c-.8-1.2-1.5-2.5-1.9-4h3.8c-.4 1.5-1.1 2.8-1.9 4zm2.3-6H9.7a14 14 0 0 1 0-4h4.6a14 14 0 0 1 0 4zm.3 5.9c.6-1.2 1-2.5 1.3-3.9h3a8 8 0 0 1-4.3 3.9zm1.7-5.9a16 16 0 0 0 0-4h3.4a8 8 0 0 1 0 4z"/></svg>
        www.brimphysio.com.au
      </li>
      <li>
        <svg viewBox="0 0 24 24" aria-hidden="true"><path d="M3 5h18v14H3zm2 2v.5l7 4.5 7-4.5V7zm0 2.9V17h14V9.9l-7 4.5z"/></svg>
        nora@brimphysio.com.au
      </li>
    </ul>
    <div class="appointment">
      <div class="appointment__field"><span>Date:</span><span class="appointment__line"></span></div>
      <div class="appointment__field"><span>Time:</span><span class="appointment__line"></span></div>
    </div>
  </section>

  <section class="card card--front" aria-label="Card front">
    <div class="brand">
      <span class="brand__dot"></span>
      <span class="brand__name">Brim<br>Physiotherapy</span>
    </div>
    <p class="tagline">womens health and pelvic floor physiotherapy<br>www.brimphysio.com.au</p>
  </section>

</main>
</body>
</html>
```